Harbinger Noble Alloys Works Business Cards

We are wanting to have a new business card designed for our company as we go to a convention. We want to balance business/Modern with elegance and beauty. Our company sells highend jewelry pieces. We want to utilize the colors of Black and Gold and have gold foiled fonts to be physically printed on the business cards.
We also would like to have space to write notes on the back side of the business card. When we meet people at jewelry conventions we would like to write notes if possible.
Here are websites and designs that we like the look and feel of these companies and you can use these as design ideas.
https://www.lorvanne.com
https://www.bellquist.com/en-us/home
Here is our company website link
www.harbingernaw.com
I also up loaded two versions of our logo.
- Update 4.26.22
I have uploaded photos of a business card we like. this card has raised embossed letters that you can feel. the raise letters are like a plastic but we don't need to use that...I uploaded to show you that we like the experience of the client feeling the characters of the logo. we also would like to have the material as a satin or some material very soft.
- Maybe we can get designs with beautiful gold foiling and raised characters and logos. we like simplicity...not busy but an elegant design. We need to write notes and would like a section where we can write notes. but we want an elegant style and the client has an experience with the feel of the card when they touch the card.
Colors
- Main colors Black & Gold
- white or light colors for small notes section.
Specialty ideals and things we would like to see based on your design styles.
- raised fonts
- raised logos
- gold foiling
- satin/soft finish on the card material.
we are wanting to design a business card that looks elegant and clean. When the client is handed the business card we want them to physically experience the business card as well by touching the raised logos or fonts and the base material is soft satin. I hope this helps with further designs.
thank you all
We uploaded a new contact layout that we have designed in our office. we would like to see how this would look on your designs.
thank you
I just finished uploading the Contact Layout. the colors are just examples. please use this layout as an idea and use colors based on the feed back we have given each of you personally.
Contact Information for Business Card
we need an area to write notes, we would like to have our logos or the diamond of our logo or the business card to have embossed sections to the business card so when the customer touches the card they can feel the logo. we would also like sections of our business card to have gold foiling. we would also like to use a satin soft paper with our card. when the client touches the card its super soft and high quality
Requirements
Must have
- we would like to have our logos or the diamond of our logo or the business card to have embossed sections to the business card so when the customer touches the card they can feel the logo. we would also like sections of our business card to have gold foiling. we would also like to use a satin soft paper with our card. when the client touches the card its super soft and high quality
Nice to have
- we would like to have our logos or the diamond of our logo or the business card to have embossed sections to the business card so when the customer touches the card they can feel the logo. we would also like sections of our business card to have gold foiling.

```html
<!DOCTYPE html>
<html lang="en">
<head>
<meta charset="UTF-8">
<title>Harbinger Noble Alloys Works – Business Card</title>
<link href="https://fonts.googleapis.com/css2?family=Cinzel:wght@400;500;600&display=swap" rel="stylesheet">
<style>
  :root {
    --backdrop: #161616;
    --card: #111111;
    --card-edge: #1f1f1f;
    --gold: #c9a04c;
    --gold-soft: #a9863e;
  }
  * { margin: 0; padding: 0; box-sizing: border-box; }
  html, body {
    width: 1200px; height: 900px; overflow: hidden;
    background: var(--backdrop);
  }
  .stage {
    position: relative; width: 1200px; height: 900px;
    font-family: "Cinzel", serif; color: var(--gold);
  }
  .card {
    position: absolute; left: 250px; width: 700px; height: 400px;
    background: linear-gradient(150deg, #161616 0%, var(--card) 60%, #0c0c0c 100%);
    border: 1px solid var(--card-edge);
    box-shadow: 0 14px 30px rgba(0,0,0,0.55);
  }
  .card--front { top: 40px; }
  .card--back { top: 460px; }

  /* Front */
  .brand {
    position: absolute; left: 0; right: 0; top: 150px;
    display: flex; flex-direction: column; align-items: center; gap: 12px;
  }
  .brand__lockup { display: flex; align-items: center; gap: 14px; }
  .brand__mark { width: 14px; height: 14px; background: var(--gold); }
  .brand__name {
    font-size: 30px; font-weight: 500; letter-spacing: 1px;
  }
  .brand__tagline {
    display: flex; align-items: center; gap: 12px;
    font-size: 18px; letter-spacing: 2px; text-transform: uppercase;
  }
  .brand__rule { width: 22px; height: 1px; background: var(--gold); }

  /* Back */
  .contact-block {
    position: absolute; top: 158px; left: 0; right: 0;
    display: flex; justify-content: center; align-items: stretch; gap: 28px;
  }
  .person { text-align: right; }
  .person__name { font-size: 30px; font-weight: 500; letter-spacing: 1.5px; text-transform: uppercase; }
  .person__title { font-size: 16px; letter-spacing: 1px; color: var(--gold-soft); text-transform: uppercase; margin-top: 2px; }
  .divider { width: 1px; background: var(--gold); }
  .details { list-style: none; display: flex; flex-direction: column; gap: 4px; font-size: 16px; letter-spacing: 0.8px; }
  .details li { display: flex; align-items: center; gap: 8px; }
  .details svg { width: 13px; height: 13px; flex: none; }
</style>
</head>
<body>
<div class="stage">

  <section class="card card--front">
    <div class="brand">
      <div class="brand__lockup">
        <span class="brand__mark"></span>
        <span class="brand__name">Harbinger Noble Alloys Works</span>
      </div>
      <div class="brand__tagline">
        <span class="brand__rule"></span>
        <span>Coins, Jewelry &amp; Diamonds</span>
        <span class="brand__rule"></span>
      </div>
    </div>
  </section>

  <section class="card card--back">
    <div class="contact-block">
      <div class="person">
        <div class="person__name">Dorian Vell</div>
        <div class="person__title">CEO/Founder</div>
      </div>
      <div class="divider"></div>
      <ul class="details">
        <li>
          <svg viewBox="0 0 16 16" fill="none" stroke="#c9a04c" stroke-width="1.6"><path d="M4 1.5l2.5 3-1.5 1.8c.8 1.8 2 3 3.8 3.8l1.8-1.5 3 2.5-1.6 2.4C7 13.5 2.5 9 1.6 3.1z"/></svg>
          <span>555-014-2290</span>
        </li>
        <li>
          <svg viewBox="0 0 16 16" fill="none" stroke="#c9a04c" stroke-width="1.4"><rect x="1.5" y="3.5" width="13" height="9"/><path d="M1.5 3.5L8 9l6.5-5.5"/></svg>
          <span>info@harbingernaw.com</span>
        </li>
        <li>
          <svg viewBox="0 0 16 16" fill="none" stroke="#c9a04c" stroke-width="1.3"><circle cx="8" cy="8" r="6.5"/><ellipse cx="8" cy="8" rx="2.8" ry="6.5"/><path d="M1.5 8h13M2.5 4.8h11M2.5 11.2h11"/></svg>
          <span>www.harbingernaw.com</span>
        </li>
        <li style="padding-left:21px">
          <span>www.harbingernaw.com</span>
        </li>
      </ul>
    </div>
  </section>

</div>
</body>
</html>
```